LumaguardUSA /The Brightmore & Brightmore X

Bringing to market a revolutionay new products. UVC sanitizing machines have been used by hospitals for years in operating rooms to kill viruses and bacteria. The problem is those machines cost anywhere for $65,000 to $125,000 each machine making the proven very effective technology unavailable to most industires that need them We have made 2 models that use the exact same effective technolgy that are very affordable. Our main product is The Brightmore. Tis machine is a mobile 216w unit that can effectively treat up to 1500sq ft and kill 99.9% of viruses (Covid and bacteria in 30 minutes. This unit can be used in areas such as schools, churches, nursing homes, daycares, resturaunts, casinos(especially casino bathrooms). offices, public transport, planes, vacational Rentals, etc.
Our smaller compact but powerful unit The Brightmore X is compact and powerful and can treat areas up to 864 sq ft. this unit is for use in hotel rooms, cruise ship cabins, Ambulances, School buses, and other small areas.
We all have been seeing people using sprayers spraying unknown and untested chemicals all over surfaces. there has been no long term testing and all I can picture is kids touching these surfaces and putting their fingers in their mouths. In years this will be the asbestos, weedaway and talcum powder in the near future.
These machines eliminate the risk of those chemicals. Are completly safe and have been used by major medical facilities for years.
I am looking for a website to promote and sell these 2 products. We need to market to all the prospective types of clients that could use these and show their own customers how they have responsibly took action in tried and true technology to protect them.
The main company for these products is LumaguardUSA. We are also going to be selling this side of the business as a service business where we are looking for partners around the U.S to join our team to be able to provide UVC cleaning to clients that would rather call a professionla service to come out and sanitize their location rathe than having staff do this on their own.
Looking for the basics of a website design with a simple page where they can purchase the machines. We currently have a facebook page contest that is near end with great designs. I will attach those or links in the coming days. I need this all done, setup and hosted with the ability to have constant updates. I no absolutely know anything about coding. I can add on a constant basis wording, descriptions etc. whatever is needed.
I will upload more pictures daily.
Update- Here is some boi info for site.
About The Brightmore.
UV germicidal is limited to a single wavelength of UV-C at 253.7nm. The Brightmore 360 technology is a 216w system built to produce the very effective range with an extensive range of germicidal UVC. This extended range delivers a germicidal intensity that penetrates the cell walls of microorganisms and causes irreparable damage. That’s what makes our high Intensity mobile UVC Brightmore Machine so extremely fast and effective at reducing microbial loads like the Covid Virus.

Large Medical facilities have been using this same technology in operating rooms for years but at a cost of $65k-$125k

We have taken that same technolgy and built a system that any business or School system can use the same proven and effective technology at a price they can afford.

Why The Brightmore?

Manual cleaning leaves on average 47% of surface areas untouched. The Brightmore ensures those areas are sanitized.
No more of spraying harmful or long term untested chemicals need to be sprayed. Much like the Asbestos, weedaway and talcum powders of the past.
An extremely fast and effective addition to your cleaning & sanitzing schedule.

Time Matters!

Every second counts when you feel your school or business may have a possible issue. Roll out The Brightmore and start killing it immediately. No need to wait for staff, chemicals or delays. Set up in just minutes. Clear the area and turn it on. The Brightmore gets to work immediatley.

About US .

LumaguardUSA/The Brightmore was founded in early 2020 as the emmergence of Covid-19 began. CEO/Owner- Dale Pemberton with a over 16 yrs. in the LED lighting field has used his experience in lighting to create a reasonable priced product and service to help the everyday school or business. With years of being around and involved with all types of lighting including Germicidal lamps in Hospital settings
he created the very expensive alternative that can be used by thousands of industries to help and slow down this deadly Virus.

"Our Motto" Any technology that is available to assist should not be limited by price.

Target Market(s)

Schools both public and private, hotels, Vacation rentals, daycares, nursing homes, casinos, cruise lines

```html
<!DOCTYPE html>
<html lang="en">
<head>
<meta charset="utf-8">
<title>LumaguardUSA</title>
<link rel="stylesheet" href="https://fonts.googleapis.com/css2?family=Poppins:wght@400;500;600&family=Lato:wght@400;700&display=swap">
<style>
:root{
  --brand-blue:#1a2e9c;
  --band-blue:#0b2fae;
  --footer-blue:#2a4d9b;
  --brand-red:#c40f2c;
  --ink:#222;
  --muted:#444;
  --panel:#efefef;
  --line:#c9c9c9;
  --white:#fff;
}
*{box-sizing:border-box;margin:0;padding:0}
html,body{width:1200px;height:3747px;overflow:hidden}
body{position:relative;background:var(--white);font-family:"Lato",Arial,sans-serif;color:var(--ink)}
.abs{position:absolute}
.heading{font-family:"Poppins",Arial,sans-serif;font-weight:500;color:var(--brand-blue)}

/* header */
.site-header{left:0;top:0;width:1200px;height:121px;background:var(--white);z-index:2}
.logo-disc{left:106px;top:-10px;width:224px;height:224px;border-radius:50%;background:var(--white);z-index:3;display:flex;align-items:center;justify-content:center}
.logo-word{font-family:"Poppins",sans-serif;font-weight:600;font-size:26px;color:var(--brand-blue)}
.main-nav{right:92px;top:58px;display:flex;gap:22px;font-family:"Poppins",sans-serif;font-size:14.5px;font-weight:500;color:#111}
.main-nav .active{color:var(--brand-red)}

/* hero */
.hero{left:0;top:121px;width:1200px;height:583px;background:linear-gradient(100deg,#3e5f86 0%,#7b8ea6 45%,#a9b1ba 70%,#6f7f8e 100%)}
.hero-shade{left:0;top:121px;width:1200px;height:583px;background:rgba(20,40,90,.35)}
.hero-title{left:0;top:300px;width:1200px;text-align:center;font-family:"Poppins",sans-serif;font-size:54px;font-weight:500;color:var(--white)}
.hero-sub{left:0;top:374px;width:1200px;text-align:center;font-family:"Poppins",sans-serif;font-size:17px;line-height:27px;color:var(--white)}
.btn{display:flex;align-items:center;justify-content:center;background:var(--brand-red);color:var(--white);font-family:"Poppins",sans-serif;border-radius:4px}
.hero-btn{left:493px;top:448px;width:215px;height:64px;font-size:24px;font-weight:500}

/* welcome */
.welcome-title{left:0;top:786px;width:1200px;text-align:center;font-size:40px}
.welcome-text{left:160px;top:858px;width:880px;text-align:center;font-size:16px;line-height:36px;color:var(--muted)}

/* about */
.about-photo{left:0;top:1121px;width:500px;height:414px;background:linear-gradient(120deg,#1f55d8,#0a2a9a 60%,#133fb8)}
.about-panel{left:500px;top:1121px;width:700px;height:414px;background:var(--panel)}
.about-title{left:548px;top:1161px;font-size:34px}
.about-text{left:548px;top:1222px;width:538px;font-size:15.5px;line-height:32.3px;color:var(--muted);text-align:justify}
.about-btn{left:548px;top:1449px;width:169px;height:54px;font-size:17px}

/* why */
.why-title{left:90px;top:1667px;font-size:34px}
.why-list{left:90px;top:1740px;width:500px;list-style:none;font-size:16px;line-height:34px;color:var(--muted)}
.why-list li{position:relative;padding-left:26px}
.why-list li::before{content:"";position:absolute;left:2px;top:13px;width:7px;height:7px;border-right:1.5px solid var(--brand-blue);border-top:1.5px solid var(--brand-blue);transform:rotate(45deg)}
.why-photo{left:608px;top:1628px;width:502px;height:357px;background:linear-gradient(135deg,#2a7fd0,#5bb9e8 40%,#c8cfd6 75%,#8d959c)}

/* time band */
.time-band{left:0;top:2076px;width:1200px;height:267px;background:linear-gradient(90deg,#0c31b2,#1440c4 50%,#0a2ea8)}
.time-title{left:0;top:2110px;width:1200px;text-align:center;font-family:"Poppins",sans-serif;font-size:40px;font-weight:500;color:var(--white)}
.time-text{left:110px;top:2183px;width:980px;text-align:center;font-family:"Poppins",sans-serif;font-size:21.5px;line-height:37.5px;color:var(--white)}

/* contact */
.contact-box{left:127px;top:2432px;width:944px;height:189px;border:2px solid #ddd}
.contact-title{left:147px;top:2455px;font-size:34px}
.contact-address{left:167px;top:2515px;font-family:"Poppins",sans-serif;font-size:16.5px;line-height:32px;color:#111}
.pin{left:140px;top:2520px}
.contact-line{font-family:"Poppins",sans-serif;font-size:19.5px;display:flex;align-items:center;gap:22px}
.contact-phone{left:585px;top:2498px;color:#111}
.contact-mail{left:585px;top:2542px;color:var(--brand-blue)}
.field{border:1.5px solid #cfcfcf;background:var(--white);font-size:15.5px;color:#555;padding:0 12px;display:flex;align-items:center}
.f-name{left:127px;top:2665px;width:273px;height:56px}
.f-email{left:420px;top:2665px;width:275px;height:56px}
.f-phone{left:127px;top:2737px;width:273px;height:56px}
.f-address{left:420px;top:2737px;width:275px;height:56px;font-size:14px}
.f-comments{left:127px;top:2810px;width:570px;height:230px;align-items:flex-start;padding-top:14px}
.submit-btn{left:538px;top:3066px;width:159px;height:51px;background:var(--footer-blue);color:var(--white);font-family:"Poppins",sans-serif;font-size:16px;display:flex;align-items:center;justify-content:center}
.contact-photo{left:740px;top:2665px;width:332px;height:452px;background:linear-gradient(160deg,#4fb8c4,#1d8fa3 50%,#2f6f7a);border:2px solid #ddd}

/* footer */
.site-footer{left:0;top:3235px;width:1200px;height:445px;background:var(--panel)}
.footer-logo{left:0;top:3330px;width:1200px;text-align:center;font-family:"Poppins",sans-serif;font-weight:600;font-size:40px;color:var(--brand-blue)}
.rule{height:2px;background:var(--line)}
.rule-top{left:127px;top:3466px;width:925px}
.rule-bottom{left:137px;top:3587px;width:927px}
.social{top:3485px;display:flex;align-items:center;gap:24px;font-family:"Poppins",sans-serif;font-size:19px;color:#222}
.social-dot{width:70px;height:70px;border-radius:50%;background:var(--white);box-shadow:0 3px 8px rgba(0,0,0,.18)}
.footer-nav{left:0;top:3614px;width:1200px;display:flex;justify-content:center;gap:30px;font-family:"Poppins",sans-serif;font-size:19px;color:#111}
.footer-bar{left:0;top:3680px;width:1200px;height:67px;background:var(--footer-blue);color:#e6ebf5;font-family:"Poppins",sans-serif;font-size:17px;display:flex;align-items:center;justify-content:center}
</style>
</head>
<body>

<header class="abs site-header">
  <nav class="abs main-nav">
    <span class="active">HOME</span><span>ABOUT US</span><span>WHY THE BRIGHTMORE?</span><span>TIME MATTERS!</span><span>BLOG</span><span>CONTACT US</span>
  </nav>
</header>
<div class="abs logo-disc"><span class="logo-word">LumaguardUSA</span></div>

<section>
  <div class="abs hero" role="img" aria-label="UVC sanitizing unit in a bright office with floating virus particles"></div>
  <div class="abs hero-shade"></div>
  <h1 class="abs hero-title">LUMAGUARDUSA</h1>
  <p class="abs hero-sub">We have taken that same technolgy and built a system that any business or School system<br>can use the same proven and effective technology at a price they can afford.</p>
  <div class="abs btn hero-btn">GET STARTED</div>
</section>

<section>
  <h2 class="abs heading welcome-title">WELCOME TO LUMAGUARDUSA</h2>
  <p class="abs welcome-text">Lorem ipsum dolor sit amet, consectetur adipiscing elit, sed do eiusmod tempor incididunt ut labore et dolore magna aliqua. Ut enim ad minim veniam, quis nostrud exercitation ullamco laboris nisi ut aliquip ex ea commdo consequat. Duis aute irure dolor in reprehenderit in voluptate velit esse cillum dolore eu fugiat nulla pariatur. Ecepteur sint occae-cat cupidatat non proident, sunt in culpa qui officia deserunt mollit anim id est laborum.Ut enim ad minima veniam, quis nostrum exercitationem ullam corporis suscipit laboriosam, nisi ut aliquid</p>
</section>

<section>
  <div class="abs about-photo" role="img" aria-label="Hospital room lit by blue UVC lamps beside a bed"></div>
  <div class="abs about-panel"></div>
  <h2 class="abs heading about-title">ABOUT US</h2>
  <p class="abs about-text">Lumaguardusa/The Brightmore Was Founded In Early 2020 As The Emmer-gence Of Covid-19 Began.Ceo/Owner- Dale Pemberton With A Over 16 Yrs. In The Led Lighting Field Has Used His Experience In Lighting To Create A Reasonable Priced Product And Service To Help The Everyday School Or Business. With Years Of Being Around And Involved With All Types Of Lighting Including Germicidal Lamps In Hospital Settings</p>
  <div class="abs btn about-btn">READ MORE</div>
</section>

<section>
  <h2 class="abs heading why-title">WHY THE BRIGHTMORE?</h2>
  <ul class="abs why-list">
    <li>Manual cleaning leaves on average 47% of surface areas untouched. The Brightmore ensures those areas are sanitized.</li>
    <li>No more of spraying harmful or long term untested chemicals need to be sprayed. Much like the Asbestos, weedaway and talcum powders of the past.</li>
    <li>An extremely fast and effective addition to your cleaning &amp; sanitzing schedule.</li>
  </ul>
  <div class="abs why-photo" role="img" aria-label="Mobile UVC tower unit in a conference room with virus particles"></div>
</section>

<section>
  <div class="abs time-band"></div>
  <h2 class="abs time-title">TIME MATTERS!</h2>
  <p class="abs time-text">Every second counts when you feel your school or business may have a possible issue. Roll out the Brightmore and start killing it immediately. No need to wait for staff, chemicals or delays. Set up in just minutes. Clear the area and turn it on. The Brightmore gets to work immediatley.</p>
</section>

<section>
  <div class="abs contact-box"></div>
  <h2 class="abs heading contact-title">CONTACT US</h2>
  <svg class="abs pin" width="16" height="24" viewBox="0 0 16 24"><path d="M8 0C3.6 0 0 3.5 0 7.9 0 13.5 8 24 8 24s8-10.5 8-16.1C16 3.5 12.4 0 8 0z" fill="#2a4d9b"/><circle cx="8" cy="8" r="3" fill="#fff"/></svg>
  <p class="abs contact-address">Eichenstraße 24<br>78590 Brunnthal / Kreisau<br>Germany</p>
  <div class="abs contact-line contact-phone">
    <svg width="20" height="20" viewBox="0 0 24 24"><path d="M6.6 10.8a15 15 0 0 0 6.6 6.6l2.2-2.2c.3-.3.7-.4 1-.2 1.1.4 2.3.6 3.6.6.6 0 1 .4 1 1V20c0 .6-.4 1-1 1A17 17 0 0 1 3 4c0-.6.4-1 1-1h3.5c.6 0 1 .4 1 1 0 1.3.2 2.5.6 3.6.1.3 0 .7-.2 1z" fill="#2a4d9b"/></svg>
    <span>+555 555 0123</span>
  </div>
  <div class="abs contact-line contact-mail">
    <svg width="22" height="18" viewBox="0 0 22 18"><rect x="1" y="1" width="20" height="16" rx="2" fill="none" stroke="#2a4d9b" stroke-width="2"/><path d="M1 3l10 7 10-7" fill="none" stroke="#2a4d9b" stroke-width="2"/></svg>
    <span>info@LumaguardUSA.com</span>
  </div>

  <div class="abs field f-name">Name</div>
  <div class="abs field f-email">Email</div>
  <div class="abs field f-phone">Phone Number</div>
  <div class="abs field f-address">Address</div>
  <div class="abs field f-comments">Comments</div>
  <div class="abs submit-btn">SUBMIT</div>
  <div class="abs contact-photo" role="img" aria-label="Factory floor with rows of UVC units glowing teal"></div>
</section>

<footer>
  <div class="abs site-footer"></div>
  <div class="abs footer-logo">LumaguardUSA</div>
  <div class="abs rule rule-top"></div>
  <div class="abs social" style="left:297px"><span class="social-dot"></span><span>FACEBOOK</span></div>
  <div class="abs social" style="left:525px"><span class="social-dot"></span><span>TWITTER</span></div>
  <div class="abs social" style="left:742px"><span class="social-dot"></span><span>INSTAGRAM</span></div>
  <div class="abs rule rule-bottom"></div>
  <nav class="abs footer-nav"><span>HOME</span><span>ABOUT US</span><span>WHY THE BRIGHTMORE?</span><span>TIME MATTERS!</span><span>BLOG</span><span>CONTACT US</span></nav>
  <div class="abs footer-bar">© 2020 LumaguardUSA. - All rights reserved.</div>
</footer>

</body>
</html>
```